Figure for a research paper

I am working on designing a figure for a research paper that illustrates the effect of KORA Pathway assessment on student outcomes over time by impacting teacher bias and teacher perception of student growth. I built the attached figure via powerpoint. It includes the very basic elements but it does not look great and I am not sure that it is clearly depicting what I am hoping to illustrate. I would like for you to build an illustration of this idea that i can include in the paper.

```html
<!DOCTYPE html>
<html lang="en">
<head>
<meta charset="utf-8">
<title>KORA Pathway Assessment and Teacher Perception Over Time</title>
<link href="https://fonts.googleapis.com/css2?family=Montserrat:wght@400;500;700&display=swap" rel="stylesheet">
<style>
  :root {
    --axis: #555a60;
    --ink: #3a3a3a;
    --ink-strong: #2e2e2e;
    --red: #c22432;
    --red-soft: #f4a3a3;
    --blue: #1f77c2;
    --blue-mid: #2aa6e0;
    --blue-soft: #cfeefb;
    --green: #3cb54a;
    --green-arrow: #a6f08f;
    --green-field: #eefbe8;
    --purple: #8b2c93;
    --purple-arrow: #c49cf0;
    --purple-field: #f5effc;
    --page: #ffffff;
  }
  html, body {
    margin: 0;
    padding: 0;
    width: 1200px;
    height: 1186px;
    overflow: hidden;
    background: var(--page);
  }
  .figure {
    display: block;
    width: 1200px;
    height: 1186px;
    font-family: "Montserrat", Arial, sans-serif;
  }
  .axis-line { stroke: var(--axis); stroke-width: 1.4; fill: none; }
  .axis-head { fill: var(--axis); }
  .axis-title { font-size: 9.5px; font-weight: 700; fill: var(--ink-strong); }
  .axis-sub { font-size: 9.5px; font-weight: 400; fill: var(--ink); }
  .time-label { font-size: 10px; font-weight: 700; fill: var(--ink-strong); }
  .note { font-size: 10.5px; font-weight: 400; fill: var(--ink); }
  .note-strong { font-size: 10.5px; font-weight: 700; fill: var(--ink-strong); }
  .trend-red { stroke: var(--red); stroke-width: 2; }
  .trend-blue { stroke: var(--blue); stroke-width: 2; }
  .trend-green { stroke: var(--green); stroke-width: 2; }
  .trend-purple { stroke: var(--purple); stroke-width: 2; }
  .baseline { stroke: #333; stroke-width: 0.8; stroke-dasharray: 2 2.5; }
  .field-green { fill: var(--green-field); }
  .field-purple { fill: var(--purple-field); }
</style>
</head>
<body>
<svg class="figure" viewBox="0 0 800 790.67" xmlns="http://www.w3.org/2000/svg" role="img" aria-label="Two line charts showing effectiveness of an SEL program on the student over time, comparing KORA Pathway assessment with teacher bias and inaccurate perception of student growth">
  <defs>
    <linearGradient id="blueDown" x1="0" y1="0" x2="0" y2="1">
      <stop offset="0" stop-color="var(--blue-soft)"/>
      <stop offset="1" stop-color="var(--blue-mid)"/>
    </linearGradient>
    <linearGradient id="redUp" x1="0" y1="1" x2="0" y2="0">
      <stop offset="0" stop-color="#fde3e3"/>
      <stop offset="1" stop-color="var(--red)"/>
    </linearGradient>
    <linearGradient id="greenUp" x1="0" y1="1" x2="0" y2="0">
      <stop offset="0" stop-color="#effde8"/>
      <stop offset="1" stop-color="var(--green-arrow)"/>
    </linearGradient>
    <linearGradient id="purpleDown" x1="0" y1="0" x2="0" y2="1">
      <stop offset="0" stop-color="#f4ecfd"/>
      <stop offset="1" stop-color="var(--purple-arrow)"/>
    </linearGradient>
  </defs>

  <!-- ===== Chart one: diverging trends ===== -->
  <g class="chart chart-diverging">
    <line class="axis-line" x1="199" y1="96" x2="199" y2="312"/>
    <path class="axis-head" d="M199,88 L194,98 L204,98 Z"/>
    <line class="axis-line" x1="199" y1="312" x2="604" y2="312"/>
    <path class="axis-head" d="M613,312 L603,307 L603,317 Z"/>

    <text class="axis-title" transform="translate(175,210) rotate(-90)" text-anchor="middle">Effectiveness of SEL Program</text>
    <text class="axis-sub" transform="translate(187,210) rotate(-90)" text-anchor="middle">on the Student</text>
    <text class="time-label" x="407" y="333" text-anchor="middle">Time</text>

    <line class="trend-red" x1="199" y1="252" x2="603" y2="106"/>
    <line class="trend-blue" x1="199" y1="252" x2="603" y2="178"/>

    <g class="arrow-bias">
      <path fill="url(#blueDown)" d="M362,228 H378 V252 H385 L370,268 L355,252 H362 Z"/>
      <path fill="url(#blueDown)" d="M362,255 H378 V268 H385 L370,286 L355,268 H362 Z"/>
    </g>
    <g class="arrow-assessment">
      <path fill="url(#redUp)" d="M564,178 H580 V144 H587 L572,126 L557,144 H564 Z"/>
      <path fill="url(#redUp)" d="M564,182 H580 V166 H587 L572,148 L557,166 H564 Z"/>
    </g>
    <g class="arrow-perception">
      <path fill="url(#blueDown)" d="M564,194 H580 V230 H587 L572,248 L557,230 H564 Z"/>
      <path fill="url(#blueDown)" d="M564,246 H580 V268 H587 L572,286 L557,268 H564 Z"/>
    </g>

    <text class="note" x="272" y="274">Teacher Bias</text>
    <text class="note" text-anchor="middle">
      <tspan x="488" y="247">Teacher’s inaccurate</tspan>
      <tspan x="488" y="261">perception of student</tspan>
      <tspan x="488" y="275">growth (or learning)</tspan>
    </text>
    <text class="note-strong">
      <tspan x="601" y="143">KORA Pathway</tspan>
      <tspan x="601" y="157">Assessment</tspan>
    </text>
  </g>

  <!-- ===== Chart two: assessment field vs perception field ===== -->
  <g class="chart chart-fields">
    <polygon class="field-green" points="199,392 616,392 616,482 199,594"/>
    <polygon class="field-purple" points="199,594 616,482 616,652 199,652"/>
    <line class="baseline" x1="199" y1="594" x2="616" y2="482"/>

    <line class="axis-line" x1="199" y1="390" x2="199" y2="652"/>
    <path class="axis-head" d="M199,382 L194,392 L204,392 Z"/>
    <line class="axis-line" x1="199" y1="652" x2="617" y2="652"/>
    <path class="axis-head" d="M626,652 L616,647 L616,657 Z"/>

    <text class="axis-title" transform="translate(175,520) rotate(-90)" text-anchor="middle">Effectiveness of SEL Program</text>
    <text class="axis-sub" transform="translate(187,520) rotate(-90)" text-anchor="middle">on the Student</text>
    <text class="time-label" x="405" y="675" text-anchor="middle">Time</text>

    <g class="arrows-up">
      <path fill="url(#greenUp)" d="M262,562 H278 V548 H287 L270,530 L253,548 H262 Z"/>
      <path fill="url(#greenUp)" d="M362,542 H378 V512 H387 L370,493 L353,512 H362 Z"/>
      <path fill="url(#greenUp)" d="M464,512 H480 V480 H489 L472,460 L455,480 H464 Z"/>
      <path fill="url(#greenUp)" d="M566,490 H582 V446 H591 L574,425 L557,446 H566 Z"/>
    </g>
    <g class="arrows-down">
      <path fill="url(#purpleDown)" d="M262,584 H278 V600 H287 L270,620 L253,600 H262 Z"/>
      <path fill="url(#purpleDown)" d="M362,560 H378 V585 H387 L370,605 L353,585 H362 Z"/>
      <path fill="url(#purpleDown)" d="M464,530 H480 V564 H489 L472,585 L455,564 H464 Z"/>
      <path fill="url(#purpleDown)" d="M566,500 H582 V544 H591 L574,566 L557,544 H566 Z"/>
    </g>

    <line class="trend-green" x1="199" y1="594" x2="616" y2="444"/>
    <line class="trend-purple" x1="199" y1="594" x2="616" y2="517"/>

    <text class="note-strong" x="407" y="446" text-anchor="middle">KORA Pathway Assessment</text>
    <text class="note" x="323" y="629" text-anchor="middle">Teacher Bias</text>
    <text class="note" text-anchor="middle">
      <tspan x="508" y="613">Teacher’s inaccurate</tspan>
      <tspan x="508" y="627">perception of student</tspan>
      <tspan x="508" y="641">growth (or learning)</tspan>
    </text>
  </g>
</svg>
</body>
</html>
```